Mona Felstead

My company, toller coaching are based in surrey uk. I am looking for a design for A5 flyer to attract coaching for children and young adults.
I want to include a an image of a mother reprimading her children - a teenager and young adult front and any releant images at back.
Also my company logo at indicated at bottom of front and back but pls do not include the word consultants - please change to coaching
FRONT:
Strapline: Do you feel you’re constantly nagging your child about their behaviour and school work? Is this affecting your relationship?
Image of mother and speech bubbles:
• How can I help my child get the results they’re capable of and make the right subject choices?
• How can I help my child think for themselves and not just follow the crowd?
• How do I get my child to achieve their best academically and socially?
• How do I help my child make the right career choice for them?
Testimonials from our client prove that Personal Development Coaching can help your child:
‘Coaching improved my self-awareness and helped me make better decisions without being influenced by my peers’.
'Mona helped me to set clear and purposeful university goals at a time that I was confused. I am now at a top university and have a clear vision of my future career path’.
‘I successfully met my yearly goals by using techniques with Toller coaching, such as the wheel of life and vision boards’.
'Mona has given me the impetus that I was lacking to break down what I saw as unachievable academic ambition’.
'Toller’s coaching has helped me feel motivated, energised and confident within myself'.
Book your free consultation:
e: mona@toller-example.co.uk t: 0781 502 6614 w: www.toller-example.co.uk (include logo)
BACK: images of children of different age groups (teenagers to young adults)
Why Toller?
• Qualified Personal Development Coach
• Qualified teacher with 25 years experience in secondary schools and at university level
• Postgraduate qualification in teaching children with specific learning difficulties
Mona is a specialist in coaching for:
• Coping with peer and academic pressure
• Identifying strengths and building confidence
• Discovering an appropriate career path
• Feeling motivated and achieving potential
• Managing time and learning how to discipline one’s self
Updates
I would also liek to add my phot to flyer
I have extended the deadline
The flyer is a5 double sided
I will require my photo on the back - which I will upload
Logo image is provided but will designers provide other images

```html
<!DOCTYPE html>
<html lang="en">
<head>
<meta charset="utf-8">
<title>Toller Coaching – A5 flyer, front and back</title>
<link rel="stylesheet" href="https://fonts.googleapis.com/css2?family=Arimo:ital,wght@0,400;0,700;1,400&family=PT+Serif:wght@400;700&family=Archivo+Black&display=swap">
<style>
  :root{
    --stage:#3b2a1e;
    --paper:#ffffff;
    --sun:#fbcb2a;
    --sun-deep:#f4b81c;
    --sky:#2f7fd6;
    --sky-dark:#1f5fb8;
    --navy:#1d2b78;
    --orange:#f07a38;
    --teal:#39b6c4;
    --ink:#111111;
    --photo-warm:#d9b49a;
    --photo-cool:#9db8d0;
  }
  *{margin:0;padding:0;box-sizing:border-box}
  html,body{width:1200px;height:900px;overflow:hidden;background:var(--stage)}
  .canvas{position:relative;width:1200px;height:900px}
  .page{position:absolute;top:25px;width:586px;height:830px;background:var(--paper);overflow:hidden}
  .page--front{left:10px}
  .page--back{left:605px}
  .abs{position:absolute}
  .photo{position:absolute}

  /* FRONT */
  .front-photo-scold{left:10px;top:15px;width:186px;height:142px;
    background:linear-gradient(135deg,#f7e27a 0%,#e9c8a8 45%,#c9d6e4 100%)}
  .strapline{left:203px;top:30px;width:360px;font-family:"PT Serif",serif;font-size:17.5px;line-height:21px;color:var(--orange);letter-spacing:.2px}
  .strapline .question{color:var(--sky)}
  .front-swoosh{left:0;top:110px;width:586px;height:120px}
  .testimonial-heading{left:50px;top:246px;width:210px;text-align:center;font-family:"Arimo",sans-serif;font-weight:700;font-size:15.5px;line-height:19px;color:var(--orange);text-transform:uppercase}
  .testimonials{left:48px;top:360px;width:200px;text-align:center;font-family:"Arimo",sans-serif;font-style:italic;font-size:10.6px;line-height:13.4px;color:var(--sky)}
  .testimonials p{margin-bottom:13px}
  .front-photo-mother{left:395px;top:315px;width:191px;height:515px;
    background:linear-gradient(180deg,#e9d9b8 0%,#d8b98e 30%,#8b7b6c 70%,#6e6259 100%)}
  .thoughts{left:0;top:0;width:586px;height:830px}
  .bubble-text{position:absolute;text-align:center;font-family:"PT Serif",serif;font-weight:700;font-size:10px;line-height:11.5px;color:var(--sun)}
  .cta-front{left:46px;top:757px;font-family:"PT Serif",serif;font-size:24px;color:var(--orange)}
  .contact{font-family:"Arimo",sans-serif;font-size:11.5px;display:flex;align-items:center;gap:4px;white-space:nowrap}
  .contact svg{width:11px;height:11px;flex:none}
  .contact-front{left:46px;top:783px;color:var(--sky)}
  .brand{display:flex;flex-direction:column;align-items:center;font-family:"PT Serif",serif;font-size:15px;line-height:17px;color:var(--teal);letter-spacing:.5px}
  .brand-mark{width:14px;height:14px;border-radius:50%;background:var(--sky);margin-bottom:6px}
  .brand-front{left:400px;top:730px}
  .front-footer-bar{left:0;bottom:0;width:586px;height:7px;background:var(--sky)}

  /* BACK */
  .back-yellow{left:0;top:140px;width:586px;height:600px;background:var(--sun)}
  .back-photo-group{left:58px;top:0;width:442px;height:165px;
    background:linear-gradient(180deg,#c8a48a 0%,#e4c5ad 55%,rgba(251,203,42,0) 100%)}
  .why{left:0;top:152px;width:586px;text-align:center;font-family:"Archivo Black",sans-serif;font-size:44px;color:var(--sky);letter-spacing:1px;
    text-shadow:0 0 2px #fff36a,0 0 4px #fff36a,2px 2px 0 #fff36a,-2px -2px 0 #fff36a,2px -2px 0 #fff36a,-2px 2px 0 #fff36a}
  .quals{left:0;top:222px;width:586px;font-family:"Arimo",sans-serif;font-weight:700;font-size:14px;line-height:18px;color:var(--ink)}
  .quals p{position:absolute;white-space:nowrap}
  .specialist-heading{left:63px;top:428px;font-family:"Arimo",sans-serif;font-size:19px;color:var(--sky)}
  .back-photo-coach{left:63px;top:467px;width:143px;height:210px;
    background:linear-gradient(160deg,#f1ece6 0%,#c98a63 45%,#3a2a26 100%)}
  .specialisms{left:228px;top:471px;width:320px;list-style:none;font-family:"Arimo",sans-serif;font-weight:700;font-size:12px;line-height:14.5px;color:var(--ink)}
  .specialisms li{display:flex;gap:8px;margin-bottom:14.5px}
  .specialisms svg{width:16px;height:16px;flex:none;margin-top:-1px}
  .back-swoosh{left:0;top:615px;width:586px;height:215px}
  .cta-back{left:103px;top:743px;font-family:"PT Serif",serif;font-weight:700;font-size:24px;color:var(--navy)}
  .contact-back{left:70px;top:770px;color:var(--orange)}
  .brand-back{left:428px;top:712px}
</style>
</head>
<body>
<main class="canvas">

  <!-- Front of flyer -->
  <section class="page page--front">
    <div class="photo front-photo-scold" role="img" aria-label="Photo of a mother reprimanding her son"></div>

    <svg class="abs front-swoosh" viewBox="0 0 586 120" aria-hidden="true">
      <path d="M0 40 C150 70 330 80 586 0 L586 45 C380 90 170 115 0 75 Z" fill="var(--sun)"/>
      <path d="M0 75 C170 115 380 90 586 45 L586 52 C380 98 170 122 0 82 Z" fill="var(--sky)"/>
    </svg>

    <h1 class="abs strapline">Do you feel you’re constantly nagging your child about their behaviour and school work?<br><span class="question">Is this affecting your relationship?</span></h1>

    <h2 class="abs testimonial-heading">Testimonials from our client prove that Personal Development Coaching can help your child:</h2>

    <div class="abs testimonials">
      <p>‘Coaching improved my self-aware-ness and helped me make better decisions without being influenced by my peers’.</p>
      <p>'Mona helped me to set clear and pur-poseful university goals at a time that I was confused. I am now at a top university and have a clear vision of my future career path’.</p>
      <p>‘I successfully met my yearly goals by using techniques with Toller coaching, such as the wheel of life and vision boards’.</p>
      <p>'Mona has given me the impetus that I was lacking to break down what I saw as unachievable academic ambition’.</p>
      <p>'Toller’s coaching has helped me feel motivated, energised and confi-dent within myself'.</p>
    </div>

    <div class="photo front-photo-mother" role="img" aria-label="Photo of a thoughtful mother with hand on chin"></div>

    <svg class="abs thoughts" viewBox="0 0 586 830" aria-hidden="true" fill="var(--sky)">
      <ellipse cx="420" cy="235" rx="72" ry="36"/><ellipse cx="380" cy="222" rx="30" ry="22"/><ellipse cx="460" cy="218" rx="34" ry="24"/><ellipse cx="420" cy="262" rx="46" ry="18"/>
      <circle cx="469" cy="285" r="6"/><circle cx="478" cy="300" r="4.5"/><circle cx="485" cy="312" r="3.5"/>
      <ellipse cx="355" cy="315" rx="72" ry="38"/><ellipse cx="318" cy="300" rx="30" ry="22"/><ellipse cx="398" cy="298" rx="34" ry="24"/><ellipse cx="355" cy="344" rx="48" ry="18"/>
      <circle cx="440" cy="345" r="6"/><circle cx="453" cy="349" r="4.5"/><circle cx="465" cy="352" r="3.5"/>
      <ellipse cx="338" cy="405" rx="72" ry="38"/><ellipse cx="298" cy="392" rx="30" ry="22"/><ellipse cx="378" cy="388" rx="34" ry="24"/><ellipse cx="338" cy="432" rx="48" ry="18"/>
      <circle cx="420" cy="397" r="6"/><circle cx="436" cy="393" r="4.5"/><circle cx="450" cy="390" r="3.5"/>
      <ellipse cx="345" cy="498" rx="68" ry="36"/><ellipse cx="308" cy="485" rx="28" ry="21"/><ellipse cx="385" cy="482" rx="32" ry="22"/><ellipse cx="345" cy="523" rx="45" ry="17"/>
      <circle cx="410" cy="462" r="6"/><circle cx="424" cy="456" r="4.5"/><circle cx="437" cy="451" r="3.5"/>
    </svg>
    <p class="bubble-text" style="left:362px;top:206px;width:118px">How can I help my child get the results they’re capable of and make the right subject choices?</p>
    <p class="bubble-text" style="left:298px;top:287px;width:114px">How can I help my child think for themselves and not just follow the crowd?</p>
    <p class="bubble-text" style="left:280px;top:382px;width:116px">How do I get my child to achieve their best academically and socially?</p>
    <p class="bubble-text" style="left:290px;top:475px;width:112px">How do I help my child make the right career choice for them?</p>

    <p class="abs cta-front">Book your free consultation</p>
    <p class="abs contact contact-front">
      <svg viewBox="0 0 12 12"><rect x="1" y="2.5" width="10" height="7" fill="none" stroke="var(--sky)"/><path d="M1 2.5 6 7 11 2.5" fill="none" stroke="var(--sky)"/></svg>mona@toller-example.co.uk
      <svg viewBox="0 0 12 12"><rect x="3.5" y="1" width="5" height="10" rx="1" fill="var(--orange)"/></svg>0781 502 6614
      <svg viewBox="0 0 12 12"><circle cx="6" cy="6" r="5" fill="var(--orange)"/></svg>www.toller-example.co.uk
    </p>
    <div class="abs brand brand-front"><span class="brand-mark"></span><span>TOLLER</span><span>COACHING</span></div>
    <div class="abs front-footer-bar"></div>
  </section>

  <!-- Back of flyer -->
  <section class="page page--back">
    <div class="abs back-yellow"></div>
    <div class="photo back-photo-group" role="img" aria-label="Photo of a smiling group of teenagers and young adults"></div>

    <h1 class="abs why">WHY TOLLER?</h1>

    <div class="abs quals">
      <p style="left:150px;top:0">Qualified Personal Development Coach</p>
      <p style="left:139px;top:44px">Qualified teacher with 25 years experience<br>in secondary schools and at university level</p>
      <p style="left:150px;top:106px">Postgraduate qualification in teaching<br>children with specific learning difficulties</p>
    </div>

    <h2 class="abs specialist-heading">Mona is a specialist in coaching for:</h2>
    <div class="photo back-photo-coach" role="img" aria-label="Portrait photo of the coach, Mona Felstead"></div>

    <ul class="abs specialisms">
      <li><svg viewBox="0 0 16 16"><circle cx="8" cy="8" r="8" fill="var(--sky)"/><path d="M4 8.2 7 11 12.5 4.8" fill="none" stroke="#fff" stroke-width="2"/></svg>Coping with peer and academic pressure</li>
      <li><svg viewBox="0 0 16 16"><circle cx="8" cy="8" r="8" fill="var(--sky)"/><path d="M4 8.2 7 11 12.5 4.8" fill="none" stroke="#fff" stroke-width="2"/></svg>Identifying strengths and building confidence</li>
      <li><svg viewBox="0 0 16 16"><circle cx="8" cy="8" r="8" fill="var(--sky)"/><path d="M4 8.2 7 11 12.5 4.8" fill="none" stroke="#fff" stroke-width="2"/></svg>Discovering an appropriate career path</li>
      <li><svg viewBox="0 0 16 16"><circle cx="8" cy="8" r="8" fill="var(--sky)"/><path d="M4 8.2 7 11 12.5 4.8" fill="none" stroke="#fff" stroke-width="2"/></svg>Feeling motivated and achieving potential</li>
      <li><svg viewBox="0 0 16 16"><circle cx="8" cy="8" r="8" fill="var(--sky)"/><path d="M4 8.2 7 11 12.5 4.8" fill="none" stroke="#fff" stroke-width="2"/></svg>Managing time and learning how to discipline one’s self</li>
    </ul>

    <svg class="abs back-swoosh" viewBox="0 0 586 215" aria-hidden="true">
      <path d="M0 95 C200 110 360 70 586 25 L586 215 L0 215 Z" fill="var(--sky)"/>
      <path d="M0 155 C180 110 380 60 586 95 L586 215 L0 215 Z" fill="var(--sun)"/>
      <path d="M0 162 C180 118 380 68 586 103 L586 215 L0 215 Z" fill="var(--paper)"/>
    </svg>

    <p class="abs cta-back">Book your free consultation</p>
    <p class="abs contact contact-back">
      <svg viewBox="0 0 12 12"><rect x="1" y="2.5" width="10" height="7" fill="none" stroke="var(--sky)"/><path d="M1 2.5 6 7 11 2.5" fill="none" stroke="var(--sky)"/></svg>mona@toller-example.co.uk
      <svg viewBox="0 0 12 12"><rect x="3.5" y="1" width="5" height="10" rx="1" fill="var(--sky)"/></svg>0781 502 6614
      <svg viewBox="0 0 12 12"><circle cx="6" cy="6" r="5" fill="var(--sky)"/></svg>www.toller-example.co.uk
    </p>
    <div class="abs brand brand-back"><span class="brand-mark"></span><span>TOLLER</span><span>COACHING</span></div>
  </section>

</main>
</body>
</html>
```